Ceiling fan flyer design

We are after a double sided flyer design offering ceiling fan installations

Target Market(s)

Home owners

Requirements
Must have
• content listed

```html
<!DOCTYPE html>
<html lang="en">
<head>
<meta charset="utf-8">
<title>Volt Ready – Ceiling Fan Flyer</title>
<link href="https://fonts.googleapis.com/css2?family=Bangers&family=Open+Sans:ital,wght@0,300;0,400;0,600;0,700;1,300;1,400;1,600;1,700&display=swap" rel="stylesheet">
<style>
  :root {
    --orange: #f0821f;
    --paper: #ffffff;
    --backdrop: #e9e9e9;
    --headline-red: #8a1a22;
    --navy: #2b3990;
    --ink: #111111;
    --card-grey: #c9c9c9;
  }
  * { box-sizing: border-box; margin: 0; padding: 0; }
  html, body { width: 927px; height: 1200px; overflow: hidden; background: var(--backdrop); }
  body { position: relative; font-family: "Open Sans", Arial, sans-serif; }

  .flyer { position: absolute; left: 55px; top: 22px; width: 800px; height: 1138px; background: var(--paper); box-shadow: 0 2px 8px rgba(0,0,0,.25); }
  .panel { position: absolute; left: 15px; top: 0; width: 770px; height: 893px; background: var(--orange); border-radius: 0 0 22px 22px; }

  .masthead { position: absolute; left: 33px; top: 0; width: 734px; height: 213px; background: var(--paper); border-radius: 0 0 22px 22px; }
  .mascot { position: absolute; left: 30px; top: 10px; width: 160px; height: 150px; border-radius: 8px; }
  .brand-name { position: absolute; left: 22px; top: 166px; width: 180px; text-align: center; font-weight: 700; font-size: 17px; color: var(--orange); }
  .headline { position: absolute; left: 267px; top: 22px; font-family: "Bangers", Impact, sans-serif; font-style: italic; color: var(--headline-red); font-size: 62px; line-height: 57px; letter-spacing: 1px; }

  .tagline { position: absolute; left: 0; top: 220px; width: 800px; text-align: center; color: var(--navy); font-weight: 700; font-style: italic; font-size: 29px; }
  .intro { position: absolute; left: 0; top: 262px; width: 800px; text-align: center; color: var(--ink); font-weight: 700; font-size: 20.5px; line-height: 30px; }

  .testimonials { position: absolute; left: 60px; top: 345px; width: 410px; text-align: center; color: var(--paper); font-size: 19.5px; line-height: 26px; }
  .testimonial { margin-bottom: 26px; }
  .testimonial q { font-style: italic; font-weight: 300; quotes: "“" "”"; }
  .testimonial cite { display: block; font-style: normal; font-weight: 700; }

  .offer { position: absolute; left: 470px; top: 350px; color: var(--navy); }
  .offer-save { font-weight: 700; font-size: 104px; line-height: 100px; letter-spacing: -3px; }
  .offer-save sup { font-size: 80px; position: relative; top: -14px; }
  .offer-amount { font-weight: 700; font-style: italic; font-size: 50px; line-height: 48px; }
  .offer-rule { font-style: italic; font-size: 39px; line-height: 38px; }
  .offer-item { font-size: 39px; line-height: 40px; }

  .promise { position: absolute; top: 612px; width: 302px; }
  .promise--left { left: 63px; }
  .promise--right { left: 407px; }
  .promise h2 { background: var(--paper); color: var(--navy); font-size: 19px; font-weight: 700; padding: 0 6px; line-height: 24px; margin-bottom: 8px; }
  .promise ul { list-style: none; color: var(--ink); font-size: 15.5px; line-height: 20.5px; }
  .promise li::before { content: "•"; padding: 0 8px 0 6px; }

  .contact-bar { position: absolute; left: 43px; top: 823px; width: 714px; height: 54px; background: var(--paper); border-radius: 12px; text-align: center; line-height: 54px; color: var(--orange); font-weight: 700; font-size: 20px; }

  .fan-photo { position: absolute; left: 125px; top: 895px; width: 540px; height: 240px; }

  .call-now { position: absolute; left: 13px; top: 1020px; font-family: "Bangers", Impact, sans-serif; font-style: italic; line-height: 36px; }
  .call-now-label { color: var(--ink); font-size: 34px; }
  .call-now-number { color: var(--headline-red); font-size: 36px; }
  .payment-cards { position: absolute; left: 15px; top: 1093px; display: flex; gap: 4px; }
  .payment-card { width: 44px; height: 27px; background: var(--card-grey); border: 1px solid #999; }

  .conditions { position: absolute; right: 20px; top: 1068px; width: 300px; text-align: right; color: var(--headline-red); font-style: italic; font-weight: 700; font-size: 12.5px; line-height: 17px; }
</style>
</head>
<body>
  <article class="flyer">
    <div class="panel"></div>

    <header class="masthead">
      <svg class="mascot" role="img" aria-label="Illustration of a caped electrician superhero holding up a light bulb" viewBox="0 0 160 150">
        <defs><linearGradient id="mascotTone" x1="0" y1="0" x2="1" y2="1"><stop offset="0" stop-color="#cfe6f5"/><stop offset="1" stop-color="#6fae5a"/></linearGradient></defs>
        <rect width="160" height="150" rx="8" fill="url(#mascotTone)"/>
      </svg>
      <div class="brand-name">Volt Ready Pty Ltd</div>
      <h1 class="headline">HOT...<br>SWEATY...<br>UNCOMFORTABLE?</h1>
    </header>

    <p class="tagline">A breeze without the cost!</p>
    <p class="intro">Enjoy the gentle breeze &amp; cooling effect of a ceiling fan to help<br>you sleep soundly at night &amp; be more productive during the day.</p>

    <section class="testimonials">
      <blockquote class="testimonial"><q>We can now sleep! Wow what a difference! Thanks Marcus for your help.</q><cite>Graham &amp; Ruth Ellery</cite></blockquote>
      <blockquote class="testimonial"><q>Super service! What a pleasant change. Marcus could not have done more to ensure our satisfaction..</q><cite>Tom &amp; Lucia Hartley</cite></blockquote>
    </section>

    <section class="offer">
      <div class="offer-save">SAVE<sup>*</sup></div>
      <div class="offer-amount">$25 OFF</div>
      <div class="offer-rule">every second</div>
      <div class="offer-item">fan installed</div>
    </section>

    <section class="promise promise--left">
      <h2>We guarantee to...</h2>
      <ul>
        <li>Always be on time, or we pay you $100</li>
        <li>Tell you the exact cost before any job begins</li>
        <li>Provide you with a fixed price guarantee, assuring you</li>
      </ul>
    </section>
    <section class="promise promise--right">
      <h2>Have no extra costs...</h2>
      <ul>
        <li>Leave your place as clean as it was when we first arrived</li>
        <li>Return, and fix it for free, if its not right</li>
        <li>Return your telephone calls promptly</li>
        <li>Provide a minimum 12 Month warranty on all parts</li>
        <li>Provide friendly, helpful service and advice</li>
      </ul>
    </section>

    <div class="contact-bar">1300 555 014 • www.voltready.com.au • LIC NO: 104582A</div>

    <svg class="fan-photo" role="img" aria-label="Photo of a white five-blade ceiling fan with a three-lamp light kit" viewBox="0 0 540 240">
      <defs><radialGradient id="fanTone" cx="0.5" cy="0.45" r="0.55"><stop offset="0" stop-color="#efefef"/><stop offset="1" stop-color="#ffffff"/></radialGradient></defs>
      <rect width="540" height="240" fill="url(#fanTone)"/>
    </svg>

    <div class="call-now">
      <div class="call-now-label">CALL NOW</div>
      <div class="call-now-number">1300 555 027</div>
    </div>
    <div class="payment-cards">
      <span class="payment-card"></span><span class="payment-card"></span><span class="payment-card"></span>
    </div>

    <p class="conditions">*Conditions: Mention this AD when booking to receive offer. Limit one per household. Cannot be combined with any other offer.</p>
  </article>
</body>
</html>
```